Business card with professional look

I would like a creative yet professional looking business card for our business. We sell broadcast TV related security products for mobile phones, set top boxes, and tablets. Our customers are international. We have a logo we like and I would like to possibly add some color to the business card but keep it professional looking.

Target Market(s)

Professionals in the TV, cable, ans Satellite industries

Industry/Entity Type

Cable Tv

Contact Information for Business Card

Name Ned Vastermill, title CEO, Address 8130 Harborline Court, Suite 400, Del Arvo, CA 91584 USA, phone numbers m:+1.619.284.7302 o:+1.855.672.9140, email, logo

Font styles to use
Other font styles liked:
• Open to any font that looks good with logo

Requirements
Must have
• professional look with colors coordinated with logo colors. would like to add one or two different colors as well as some form of background color

```html
<!DOCTYPE html>
<html lang="en">
<head>
<meta charset="utf-8">
<title>Vantacast Business Card</title>
<link href="https://fonts.googleapis.com/css2?family=Lato:wght@400;700;900&display=swap" rel="stylesheet">
<style>
  :root {
    --backdrop: #3d3d3d;
    --card-white: #ffffff;
    --blue-light: #2aa0dc;
    --blue-mid: #1a7cc4;
    --blue-deep: #0a4f9a;
    --text-white: #ffffff;
    --icon-blue: #7cc4ef;
  }
  * { margin: 0; padding: 0; box-sizing: border-box; }
  html, body {
    width: 1200px;
    height: 810px;
    overflow: hidden;
    background: var(--backdrop);
    font-family: "Lato", sans-serif;
  }
  .sheet {
    width: 1200px;
    height: 810px;
    display: flex;
    align-items: center;
    justify-content: center;
    gap: 40px;
  }
  .card {
    width: 540px;
    height: 309px;
    position: relative;
    box-shadow: 0 6px 18px rgba(0, 0, 0, 0.35);
  }
  .card-back { background: var(--card-white); }
  .card-front {
    background: linear-gradient(160deg, var(--blue-light) 0%, var(--blue-mid) 45%, var(--blue-deep) 100%);
    color: var(--text-white);
  }
  .brand {
    position: absolute;
    top: 42px;
    right: 40px;
    display: flex;
    align-items: center;
    gap: 10px;
  }
  .brand-name {
    font-weight: 900;
    font-size: 34px;
    letter-spacing: -0.5px;
    color: var(--text-white);
  }
  .brand-square {
    width: 26px;
    height: 26px;
    background: var(--text-white);
    border-radius: 3px;
  }
  .person {
    position: absolute;
    left: 40px;
    top: 112px;
  }
  .person-name { font-size: 17px; font-weight: 400; }
  .person-title { font-size: 13px; margin-top: 2px; padding-left: 12px; }
  .address {
    position: absolute;
    left: 58px;
    top: 178px;
    font-size: 12.5px;
    line-height: 1.45;
  }
  .address .indent-1 { padding-left: 10px; }
  .address .indent-2 { padding-left: 20px; }
  .contacts {
    position: absolute;
    left: 86px;
    top: 238px;
    list-style: none;
    font-size: 12.5px;
    line-height: 1.45;
  }
  .contacts li { display: flex; align-items: center; gap: 5px; }
  .contacts svg { width: 11px; height: 11px; fill: var(--icon-blue); flex: none; }
</style>
</head>
<body>
  <main class="sheet">
    <section class="card card-back" aria-label="Card back"></section>

    <section class="card card-front" aria-label="Card front">
      <div class="brand">
        <span class="brand-name">Vantacast</span>
        <span class="brand-square"></span>
      </div>

      <div class="person">
        <p class="person-name">Ned Vastermill</p>
        <p class="person-title">CEO</p>
      </div>

      <address class="address" style="font-style:normal">
        <p>8130 Harborline Court</p>
        <p class="indent-1">Suite 400</p>
        <p class="indent-2">Del Arvo, CA 91584 USA</p>
      </address>

      <ul class="contacts">
        <li>
          <svg viewBox="0 0 24 24" aria-hidden="true"><path d="M6.6 10.8a15.1 15.1 0 0 0 6.6 6.6l2.2-2.2c.3-.3.7-.4 1-.2 1.1.4 2.3.6 3.6.6.6 0 1 .4 1 1V20c0 .6-.4 1-1 1C10.6 21 3 13.4 3 4c0-.6.4-1 1-1h3.5c.6 0 1 .4 1 1 0 1.3.2 2.5.6 3.6.1.3 0 .7-.2 1z"/></svg>
          +1.619.284.7302
        </li>
        <li>
          <svg viewBox="0 0 24 24" aria-hidden="true"><path d="M7 2h10a2 2 0 0 1 2 2v16a2 2 0 0 1-2 2H7a2 2 0 0 1-2-2V4a2 2 0 0 1 2-2zm0 3v13h10V5zm5 14.2a.9.9 0 1 0 0 1.8.9.9 0 0 0 0-1.8z"/></svg>
          +1.855.672.9140
        </li>
        <li>
          <svg viewBox="0 0 24 24" aria-hidden="true"><path d="M3 5h18a1 1 0 0 1 1 1v12a1 1 0 0 1-1 1H3a1 1 0 0 1-1-1V6a1 1 0 0 1 1-1zm1 2.2V17h16V7.2l-8 5.3z"/></svg>
          info@vantacast.com
        </li>
      </ul>
    </section>
  </main>
</body>
</html>
```